RB Business Card Design

My company provides advising/training and coaching services to business owners who want better financial results and better work/life balance. We help them through creating custom plans supported with education, strategic thinking and accountability.

We also help through some online courses which are geared to smaller businesses.
Updates

please also include our nth american contact # +1 555 382 6071

Industry/Entity Type

Financial

Contact Information for Business Card

Perry Valdane
perry@perryvaldane.net
+61 455 713 902
www.perryvaldane.net

```html
<!DOCTYPE html>
<html lang="en">
<head>
<meta charset="utf-8">
<title>Perry Valdane – Business Cards</title>
<link rel="stylesheet" href="https://fonts.googleapis.com/css2?family=Open+Sans:wght@300;400;600&display=swap">
<style>
  :root {
    --page-bg: #e6e6e4;
    --card-white: #f7f7f7;
    --brand-blue: #1f77c9;
    --wordmark-grey: #8b8e92;
    --ink-dark: #2b2b2b;
    --text-white: #ffffff;
  }
  * { margin: 0; padding: 0; box-sizing: border-box; }
  html, body {
    width: 1200px; height: 900px; overflow: hidden;
    background: var(--page-bg);
    font-family: "Open Sans", Arial, sans-serif;
  }
  .canvas {
    width: 1200px; height: 900px;
    display: flex; flex-direction: column;
    align-items: center; justify-content: center; gap: 44px;
  }
  .card {
    position: relative;
    width: 640px; height: 366px;
    background: var(--card-white);
    box-shadow: 0 6px 18px rgba(0,0,0,0.14);
    overflow: hidden;
  }
  .accent-panel { position: absolute; inset: 0; }

  /* Front */
  .contact-list {
    position: absolute; left: 26px; top: 104px;
    list-style: none; color: var(--text-white);
    font-size: 15px; line-height: 23px; font-weight: 400;
  }
  .contact-list li { display: flex; align-items: center; gap: 9px; white-space: nowrap; }
  .contact-icon { width: 13px; height: 13px; flex: none; }
  .owner-name {
    position: absolute; right: 30px; top: 26px;
    font-size: 17px; font-weight: 600; color: var(--ink-dark);
  }
  .brand { position: absolute; display: flex; align-items: center; }
  .brand-mark { border-radius: 50%; background: var(--brand-blue); flex: none; }
  .brand-name {
    font-weight: 300; text-transform: uppercase;
    color: var(--wordmark-grey); letter-spacing: 1px; white-space: nowrap;
  }
  .brand--front { left: 150px; top: 272px; gap: 14px; }
  .brand--front .brand-mark { width: 34px; height: 34px; }
  .brand--front .brand-name { font-size: 38px; }

  /* Back */
  .brand--back { inset: 0; justify-content: center; gap: 20px; }
  .brand--back .brand-mark { width: 54px; height: 54px; }
  .brand--back .brand-name { font-size: 46px; }
</style>
</head>
<body>
<main class="canvas">

  <section class="card card--front" aria-label="Business card front">
    <svg class="accent-panel" viewBox="0 0 640 366" role="img" aria-label="Decorative blue accent area">
      <polygon points="0,0 480,0 300,215 0,245" fill="var(--brand-blue)"/>
    </svg>

    <p class="owner-name">Perry Valdane</p>

    <ul class="contact-list">
      <li>
        <svg class="contact-icon" viewBox="0 0 16 16" aria-hidden="true"><path fill="#fff" d="M3.5 1 6 3.5 4.6 5.6c.8 1.9 2.4 3.6 4.3 4.5L11 8.6l2.6 2.4-1.3 2.6C6.6 13.7 2.3 9.4 1.8 3.6Z"/></svg>
        +61 455 713 902
      </li>
      <li>
        <svg class="contact-icon" viewBox="0 0 16 16" aria-hidden="true"><path fill="#fff" d="M3.5 1 6 3.5 4.6 5.6c.8 1.9 2.4 3.6 4.3 4.5L11 8.6l2.6 2.4-1.3 2.6C6.6 13.7 2.3 9.4 1.8 3.6Z"/></svg>
        +1 555 382 6071
      </li>
      <li>
        <svg class="contact-icon" viewBox="0 0 16 16" aria-hidden="true"><rect x="1" y="3" width="14" height="10" fill="#fff"/><path d="M1.5 3.5 8 9l6.5-5.5" fill="none" stroke="var(--brand-blue)" stroke-width="1.4"/></svg>
        perry@perryvaldane.net
      </li>
      <li>
        <svg class="contact-icon" viewBox="0 0 16 16" aria-hidden="true"><circle cx="8" cy="8" r="6.5" fill="none" stroke="#fff" stroke-width="1.5"/><path d="M1.5 8h13M8 1.5c-3 3.5-3 9.5 0 13M8 1.5c3 3.5 3 9.5 0 13" fill="none" stroke="#fff" stroke-width="1.2"/></svg>
        www.perryvaldane.net
      </li>
    </ul>

    <div class="brand brand--front">
      <span class="brand-mark" aria-hidden="true"></span>
      <span class="brand-name">Perry Valdane</span>
    </div>
  </section>

  <section class="card card--back" aria-label="Business card back">
    <div class="brand brand--back">
      <span class="brand-mark" aria-hidden="true"></span>
      <span class="brand-name">Perry Valdane</span>
    </div>
  </section>

</main>
</body>
</html>
```